Book and Ebook Cover for my Upcoming Book

About the Book
------------------
I need a book, ebook and if possible audio cover design for my upcoming book - Lanterns & Tides. This is my first book and really looking for a great book cover. The book is about my story, living with Mental Health and how to reclaim control of your life.

Pressmarble
-----------
I am using pressmarble.example to self-publish my book so in case of any design-related questions you can just search info on their website.

I have an initial theme I am thinking for the design book cover which I have attached. You can use this as a starting point.

Idea for the theme
---------------------
I am thinking about a phoenix to represent rising from the ashes and rebirth. The phoenix motif will be continued throughout the interior pages of the book. I'd like the cover of the book to be minimal, white with gold lettering, and maybe incorporating wings? feel free to play around with the idea and up for suggestions.

If you can think of something along these lines and make it a lot better that would be great.

What I need
---------------
The book is complete and is Trim size is 6.14 x 9.21” (234 x 156mm). I would need-
1. Book Cover
2. Back & Spine Design
3. Source File
4. Ebook Cover
5. Need multiple revisions to get the best possible outcome
6. My name and book title should also on the front cover
7. The book title should be bigger size than the subtitle

If you can give me Audiobook cover, I would love that as well and can pay extra for it if needed.

I love this for the interior phoenix motif:
https://artbazaarhub.example/VelloStudioWorks/7720418-Painted-Firebird-Graphic-Pack#fullscreen

The only other actual book cover I found online that remotely relates to what I am looking for is this -
https://www.searchloop.example/url?sa=i&url=https%3A%2F%2Fshotgallery.example%2Fkorvath&psig=BxQmTr7LK2pNvW4ZsYeHd83QaPLJ&ust=1598415525610000&source=images&cd=vfe&ved=1HXdkRmQBvubDGrTLkxbWsTqYhpTGEgcDHRRRRRHdBBBBBBCE

Target Market(s)

Personal Development
Mental health

Requirements
Must have
• 1. Book Cover
2. Back & Spine Design
3. Source File
4. Ebook Cover
Nice to have
• Audiobook cover as I eventually will be releasing the audio version of the book

```html
<!DOCTYPE html>
<html lang="en">
<head>
<meta charset="utf-8">
<title>Lanterns &amp; Tides — Front Cover</title>
<link rel="stylesheet" href="https://fonts.googleapis.com/css2?family=Josefin+Sans:wght@500;600&family=Cinzel:wght@400&display=swap">
<style>
  :root {
    --paper: #fbfaf7;
    --ink: #141414;
    --gold-light: #ecd67e;
    --gold-mid: #c9a534;
    --gold-deep: #6f530f;
    --wing-deep: #7b2e24;
    --wing-mid: #a8463a;
    --wing-red: #c93a3a;
    --flame: #e98a4a;
    --breast: #f3dc8c;
  }
  * { margin: 0; padding: 0; box-sizing: border-box; }
  html, body {
    width: 822px;
    height: 1200px;
    overflow: hidden;
    background: var(--paper);
  }
  .cover {
    position: relative;
    width: 822px;
    height: 1200px;
    background: var(--paper);
    overflow: hidden;
  }
  .title {
    position: absolute;
    top: 40px;
    left: 0;
    width: 100%;
    text-align: center;
    font-family: "Josefin Sans", sans-serif;
    font-weight: 500;
    line-height: 1;
    background: linear-gradient(180deg, var(--gold-light) 0%, var(--gold-mid) 45%, var(--gold-deep) 100%);
    -webkit-background-clip: text;
    background-clip: text;
    color: transparent;
  }
  .title-line { display: block; }
  .title-line--first { font-size: 126px; letter-spacing: 2px; }
  .title-line--amp { font-size: 90px; margin-top: 2px; }
  .title-line--second { font-size: 176px; letter-spacing: 6px; margin-top: -6px; }
  .subtitle {
    position: absolute;
    top: 428px;
    left: 0;
    width: 100%;
    text-align: center;
    font-family: "Josefin Sans", sans-serif;
    font-weight: 600;
    font-size: 25px;
    line-height: 36px;
    letter-spacing: 1px;
    color: var(--ink);
    text-transform: uppercase;
  }
  .phoenix-art {
    position: absolute;
    left: 0;
    top: 500px;
    width: 822px;
    height: 600px;
    background:
      radial-gradient(ellipse 34% 26% at 62% 54%, var(--wing-deep) 0%, rgba(123,46,36,0.55) 55%, rgba(123,46,36,0) 100%),
      radial-gradient(ellipse 22% 34% at 98% 18%, var(--wing-mid) 0%, rgba(168,70,58,0) 100%),
      radial-gradient(ellipse 12% 16% at 20% 44%, var(--flame) 0%, rgba(233,138,74,0) 100%),
      radial-gradient(ellipse 14% 30% at 4% 74%, var(--breast) 0%, rgba(243,220,140,0) 100%),
      radial-gradient(ellipse 10% 8% at 28% 68%, var(--wing-red) 0%, rgba(201,58,58,0) 100%);
  }
  .author {
    position: absolute;
    top: 1112px;
    left: 0;
    width: 100%;
    text-align: center;
    font-family: "Cinzel", serif;
    font-size: 54px;
    line-height: 1;
    letter-spacing: 1px;
    color: var(--ink);
  }
</style>
</head>
<body>
  <main class="cover">
    <h1 class="title">
      <span class="title-line title-line--first">LANTERNS</span>
      <span class="title-line title-line--amp">&amp;</span>
      <span class="title-line title-line--second">TIDES</span>
    </h1>
    <p class="subtitle">Calm your restless mind, rebuild<br>your days and gently light your way</p>
    <div class="phoenix-art" role="img" aria-label="Watercolour phoenix with a wide crimson and brown wing sweeping up to the right, its flame-coloured head bowed at the left"></div>
    <p class="author">Imara Vell</p>
  </main>
</body>
</html>
```